Generative AI radar Infographics

I want to create an infographic called "Machine Learning Prospect Compass for Tender Replies". (see slide 3 of the PowerPoint file). I want to use it on social media (ConnectHub and Website). I added 2 inspiration graphics in my brief (see slide 2 of the PowerPoint). I want to add my logo on the infographic. (I also uploaded my company logos). You can find model detailed instructions on slide 1 of the PowerPoint.
Business development and sales
I am a business consultant. I will be using this infographics on Connecthub and in my powerpoint presentations to clients

```html
<!DOCTYPE html>
<html lang="en">
<head>
<meta charset="utf-8">
<title>Machine Learning Prospect Compass for Tender Replies</title>
<link href="https://fonts.googleapis.com/css2?family=Cinzel:wght@500;700&family=Poppins:wght@400;600;700&display=swap" rel="stylesheet">
<style>
  :root {
    --navy: #0c2d45;
    --blue: #1492c0;
    --blue-light: #2aa7d3;
    --ink: #111a22;
    --paper: #ffffff;
    --map: #f3f4f6;
    --silver-1: #ffffff;
    --silver-2: #d4d7db;
    --silver-3: #a9aeb4;
  }
  * { margin: 0; padding: 0; box-sizing: border-box; }
  html, body { width: 1200px; height: 854px; overflow: hidden; background: var(--paper); }
  .poster { position: relative; width: 1200px; height: 854px; background: var(--paper); font-family: "Poppins", sans-serif; }
  .poster svg.wheel { position: absolute; inset: 0; }

  .brand { position: absolute; left: 86px; top: 66px; display: flex; align-items: center; gap: 12px; }
  .brand-dot { width: 34px; height: 34px; border-radius: 50%; background: var(--blue); }
  .brand-name { font-family: "Cinzel", serif; font-weight: 700; font-size: 22px; color: var(--navy); letter-spacing: 1px; }

  .axis { position: absolute; color: var(--ink); font-size: 22px; line-height: 24px; white-space: nowrap; }
  .axis strong { font-weight: 700; display: block; }
  .axis span { font-weight: 400; display: block; }
  .axis-top { left: 643px; top: 48px; font-weight: 700; }
  .axis-bottom { left: 288px; top: 775px; font-weight: 700; }
  .axis-left { left: 56px; top: 463px; }
  .axis-right { left: 985px; top: 463px; }

  .task-list { position: absolute; list-style: none; color: #fff; font-size: 13px; line-height: 14px; white-space: nowrap; }
  .task-list li { position: relative; padding-left: 16px; margin-bottom: 6px; }
  .task-list li::before { content: ""; position: absolute; left: 0; top: 3px; width: 8px; height: 8px; border-radius: 50%; background: var(--blue-light); border: 1.5px solid #8fd6ef; }
  .on-blue li::before { background: var(--navy); border-color: #5fc3e6; }
</style>
</head>
<body>
<div class="poster">
  <svg class="wheel" viewBox="0 0 1200 854" width="1200" height="854">
    <defs>
      <radialGradient id="hub-face" cx="45%" cy="35%" r="70%">
        <stop offset="0" stop-color="var(--silver-1)"/>
        <stop offset="0.7" stop-color="#eceef0"/>
        <stop offset="1" stop-color="var(--silver-2)"/>
      </radialGradient>
      <linearGradient id="hub-rim" x1="0" y1="0" x2="0" y2="1">
        <stop offset="0" stop-color="var(--silver-1)"/>
        <stop offset="1" stop-color="var(--silver-3)"/>
      </linearGradient>
      <path id="arc-tl" d="M 282 430 A 318 318 0 0 1 600 112"/>
      <path id="arc-tr" d="M 600 112 A 318 318 0 0 1 918 430"/>
      <path id="arc-br" d="M 918 430 A 318 318 0 0 1 600 748"/>
      <path id="arc-bl" d="M 282 430 A 318 318 0 0 0 600 748"/>
    </defs>

    <rect role="img" aria-label="Faint world map in the background" x="40" y="190" width="1130" height="560" rx="120" fill="var(--map)"/>

    <polygon points="600,40 640,88 560,88" fill="var(--navy)"/>
    <polygon points="600,818 640,770 560,770" fill="var(--navy)"/>
    <polygon points="176,421 228,382 228,460" fill="var(--blue)"/>
    <polygon points="1024,421 972,382 972,460" fill="var(--blue)"/>

    <!-- top-left: decision support -->
    <path d="M 600 430 L 244 430 A 356 356 0 0 1 600 74 Z" fill="var(--navy)"/>
    <path d="M 600 430 L 260 430 A 340 340 0 0 1 600 90 Z" fill="var(--blue)"/>
    <path d="M 600 430 L 304 430 A 296 296 0 0 1 600 134 Z" fill="var(--navy)"/>

    <!-- top-right: proposal development -->
    <path d="M 600 430 L 600 74 A 356 356 0 0 1 956 430 Z" fill="var(--blue)"/>
    <path d="M 600 430 L 600 90 A 340 340 0 0 1 940 430 Z" fill="var(--navy)"/>
    <path d="M 600 430 L 600 134 A 296 296 0 0 1 896 430 Z" fill="var(--blue)"/>

    <!-- bottom-right: proposal strategy -->
    <path d="M 600 430 L 956 430 A 356 356 0 0 1 600 786 Z" fill="var(--navy)"/>
    <path d="M 600 430 L 940 430 A 340 340 0 0 1 600 770 Z" fill="var(--blue)"/>
    <path d="M 600 430 L 896 430 A 296 296 0 0 1 600 726 Z" fill="var(--navy)"/>

    <!-- bottom-left: capture strategy -->
    <path d="M 600 430 L 600 786 A 356 356 0 0 1 244 430 Z" fill="var(--navy)"/>
    <path d="M 600 430 L 600 770 A 340 340 0 0 1 260 430 Z" fill="var(--blue)"/>
    <path d="M 600 430 L 600 726 A 296 296 0 0 1 304 430 Z" fill="var(--navy)"/>
    <path d="M 600 430 L 600 720 A 290 290 0 0 1 310 430 Z" fill="var(--blue)"/>

    <rect x="590" y="62" width="20" height="736" fill="var(--paper)"/>
    <rect x="232" y="420" width="736" height="20" fill="var(--paper)"/>

    <g font-family="Poppins, sans-serif" font-weight="700" font-size="19" letter-spacing="3" dominant-baseline="middle">
      <text fill="#fff"><textPath href="#arc-tl" startOffset="50%" text-anchor="middle">DECISION SUPPORT</textPath></text>
      <text fill="#fff"><textPath href="#arc-tr" startOffset="50%" text-anchor="middle">PROPOSAL DEVELOPMENT</textPath></text>
      <text fill="#fff"><textPath href="#arc-br" startOffset="50%" text-anchor="middle">PROPOSAL STRATEGY</textPath></text>
      <text fill="var(--navy)"><textPath href="#arc-bl" startOffset="50%" text-anchor="middle">CAPTURE STRATEGY</textPath></text>
    </g>

    <circle cx="600" cy="430" r="160" fill="url(#hub-rim)"/>
    <circle cx="600" cy="430" r="146" fill="url(#hub-face)"/>
    <circle cx="600" cy="345" r="22" fill="none" stroke="var(--blue)" stroke-width="5"/>
    <g text-anchor="middle">
      <text x="600" y="402" font-family="Cinzel, serif" font-weight="500" font-size="22" fill="var(--blue)">MACHINE LEARNING</text>
      <text x="600" y="430" font-family="Cinzel, serif" font-weight="500" font-size="22" fill="var(--blue)">PROSPECT COMPASS</text>
      <text x="600" y="460" font-family="Poppins, sans-serif" font-weight="700" font-size="22" fill="var(--navy)">FOR TENDER</text>
      <text x="600" y="487" font-family="Poppins, sans-serif" font-weight="700" font-size="22" fill="var(--navy)">REPLIES</text>
    </g>
  </svg>

  <div class="brand">
    <span class="brand-dot"></span>
    <span class="brand-name">NOVALINE ADVISORY GROUP</span>
  </div>

  <div class="axis axis-top">Process enhancement</div>
  <div class="axis axis-bottom">Strategy Enablement</div>
  <div class="axis axis-left"><strong>Insights<br>generation</strong><span>(Transformative<br>application)</span></div>
  <div class="axis axis-right"><strong>Task<br>Automation</strong><span>(foundational<br>use)</span></div>

  <ul class="task-list" style="left:442px; top:197px;">
    <li>Bid/No Bid Analysis</li>
    <li>Bid Qualification</li>
    <li>Opportunity<br>assessment</li>
  </ul>
  <ul class="task-list" style="left:330px; top:309px;">
    <li>Win Probability<br>modeling</li>
    <li>Strategic Pricing<br>optimization</li>
    <li>Compliance<br>assessment</li>
  </ul>

  <ul class="task-list on-blue" style="left:640px; top:165px;">
    <li>Proposal<br>Development</li>
    <li>CV &amp; Resumes</li>
    <li>Past Performance</li>
    <li>Technical solution</li>
    <li>Compliance Matrix</li>
  </ul>
  <ul class="task-list on-blue" style="left:776px; top:272px;">
    <li>Statement<br>of Work</li>
    <li>Executive<br>Summary</li>
    <li>Security<br>Questionnaires</li>
    <li>Due Diligence<br>Questionnaires</li>
  </ul>

  <ul class="task-list" style="left:780px; top:480px;">
    <li>Proposal plan</li>
    <li>Proposal outline</li>
    <li>Differentiators</li>
  </ul>
  <ul class="task-list" style="left:645px; top:602px;">
    <li>Win Theme<br>extraction</li>
    <li>Key messages</li>
  </ul>

  <ul class="task-list on-blue" style="left:342px; top:472px;">
    <li>Capture Plan</li>
    <li>SWOT Analysis</li>
    <li>Customer Hot<br>Buttons</li>
  </ul>
  <ul class="task-list on-blue" style="left:452px; top:586px;">
    <li>Customer<br>Intelligence</li>
    <li>Competitive<br>Intelligence</li>
    <li>Value Proposition</li>
  </ul>
</div>
</body>
</html>
```